El Molinete Postcard

Please refer to our site for inspiration - I know this is alot of info but ?

El Molinete Reception Hall
4187C Quillmont Rd, Benicia, CA 707-555-0142
www.El-Molinete.example

Located in Benicia, California, we are a new venue that can host a variety of events. We can provide an exceptional space for your next party, reception, quinceañera, birthday party, or meeting! We treat each client with respect and go out of our way to accommodate all of your needs and make your event a success. Conveniently located just off the 680/780 junction, El Molinete is located in a safe, well-lit area with a large private parking area.

The space comes prepared with everything you need to get your party started – chairs and tables with tablecloths, a well-equipped kitchen, and incredible decorations to set the perfect backdrop to your event! Rent just the Lounge for a more intimate get-together, or add the Main Hall for your large sit-down event.

Lounge – Beautiful 1,600 ft2 entry room featuring large living room with conversation sofa seating for 40+ Sound system  Pass-through bar with seating  Fully-equipped 200 ft2 kitchen with
4-burner gas stove, oven, large double sink, full-size refrigerator, 2 microwaves, and ice machine, plus lots of storage and counter space  Newly-remodeled Men’s and Women’s bathrooms

Main Hall – Spacious 24’x80’ room with seating for up to 160 people  2,000 ft2  72” round tables with chairs, each seating up to 8 guests  DJ stand and Sound system  Atmospheric lighting
_______________________________________
Pricing -
Daytime Parties
Available 8AM-2PM
4-hour minimum

Lounge and Kitchen Only
Fri - Sat - Sun : $80/hr
Mon - Thurs : $60/hr

All Areas: Lounge, Kitchen, Main Hall, and Backyard
Fri - Sat - Sun : $120/hr
Mon - Thurs : $100/hr
___________________________________________
Evening Events
Available 3PM-12AM
5-hour minimum

Lounge and Kitchen Only -
Fri - Sat - Sun : $100/hr
Mon - Thurs : $50/hr

Fri - Sat - Sun : $160/hr
Mon - Thurs : $75/hr
___________________________________________________
Looking for a different time frame, all-day rental, or other special request? Let us know!
We'd be happy to provide you with a custom quote for your event.

I am not going to mail this postcard - only a hand out I need info and pricing on back

This is a hand out - will not be mailed

Only need my text on back

• Text and pricing on back
• Vintage feel to it

```html
<!DOCTYPE html>
<html lang="en">
<head>
<meta charset="utf-8">
<title>El Molinete Postcard</title>
<link rel="stylesheet" href="https://fonts.googleapis.com/css2?family=Courgette&family=Dancing+Script:wght@500;700&family=Lato:ital,wght@0,400;0,700;1,700&family=Lobster&display=swap">
<style>
  :root{
    --brown-dark:#3e2a1a;
    --brown:#5a3e26;
    --brown-light:#8a6238;
    --beige:#f1dcc0;
    --beige-light:#f8ecdc;
    --cream:#fffaf2;
    --red:#d0222a;
    --pink:#f2b49a;
    --ink:#2b211a;
    --dot:#9a7048;
    --stage:#e9e6e2;
  }
  *{box-sizing:border-box;margin:0;padding:0}
  html,body{width:900px;height:1200px;overflow:hidden;background:var(--stage)}
  .canvas{position:relative;width:900px;height:1200px}
  .card{position:absolute;overflow:hidden;box-shadow:0 4px 14px rgba(0,0,0,.25)}
  .card svg.shapes{position:absolute;inset:0}
  .photo{position:absolute}

  /* front */
  .front{left:105px;top:50px;width:680px;height:525px;background:var(--beige)}
  .front .brand{position:absolute;left:36px;top:22px;font:700 56px/1.3 "Dancing Script",cursive;color:#fff}
  .front .offer{position:absolute;left:44px;top:142px;font-family:"Lobster",cursive;font-weight:400;text-shadow:2px 2px 0 #fff,3px 3px 4px rgba(0,0,0,.3)}
  .front .offer .lead{display:block;font-size:31px;color:var(--brown-dark);line-height:1.2}
  .front .offer .big{display:block;font-size:42px;color:var(--red);line-height:1.25}
  .front .hall{position:absolute;left:30px;top:372px;font:700 37px/1.15 "Dancing Script",cursive;color:#fff}
  .front .hall span{display:block;color:var(--pink);font-size:31px}
  .front .url{position:absolute;left:26px;top:487px;font:700 italic 16px/1 "Dancing Script",cursive;color:var(--ink);letter-spacing:.5px}

  /* back */
  .back{left:95px;top:630px;width:680px;height:520px;background:#fff}
  .back .tag{position:absolute;left:22px;top:22px;width:218px;height:34px;border-radius:0 17px 17px 0;background:var(--brown-dark);color:#fff;font:21px/34px "Courgette",cursive;padding-left:8px}
  .back .details{position:absolute;left:30px;top:68px;width:345px;font:14.4px/1.29 "Lato",sans-serif;color:var(--ink)}
  .back .details p+p{margin-top:20px}
  .back .details b{font-style:italic;font-weight:700;font-size:16px}
  .bullet{display:inline-block;width:7px;height:7px;border-radius:50%;background:var(--dot);margin:0 4px 1px}
  .back .ribbon-text{position:absolute;left:66px;top:340px;font:21px/1 "Courgette",cursive;color:#fff}
  .back .contact{position:absolute;left:28px;top:440px;list-style:none;font:italic 15px/1 "Courgette",cursive;color:#fff}
  .back .contact li{display:flex;align-items:center;gap:12px;height:26px}
  .back .contact svg{width:15px;height:15px;fill:#fff}
  .back .sign{position:absolute;left:278px;top:460px;font:500 30px/1 "Dancing Script",cursive;color:var(--beige)}

  /* pricing */
  .pricing{position:absolute;left:448px;top:18px;width:218px;padding:10px 12px;background:rgba(255,250,242,.9);border:1px solid var(--brown-light);border-radius:4px;font:11.5px/1.3 "Lato",sans-serif;color:var(--ink)}
  .pricing h3{font:400 22px/1.2 "Courgette",cursive;color:var(--brown-dark);text-align:center;margin-bottom:2px}
  .pricing h4{font:400 15px/1.3 "Courgette",cursive;color:var(--red);margin-top:4px}
  .pricing .when{font-style:italic;color:var(--brown);margin-bottom:2px}
  .pricing .area{font-weight:700;margin-top:3px}
  .pricing .rate{display:flex;justify-content:space-between}
  .pricing .rate span:last-child{font-weight:700;color:var(--brown-dark)}
  .pricing hr{border:0;border-top:1px dashed var(--dot);margin:6px 0 2px}
  .pricing .note{margin-top:6px;font-style:italic;font-size:11px;color:var(--brown)}
</style>
</head>
<body>
<main class="canvas">

  <section class="card front" aria-label="Postcard front">
    <svg class="shapes" width="680" height="525" viewBox="0 0 680 525">
      <defs>
        <linearGradient id="brownBand" x1="0" x2="1">
          <stop offset="0" stop-color="#3e2a1a"/><stop offset=".55" stop-color="#6a4a2c"/><stop offset="1" stop-color="#4a321e"/>
        </linearGradient>
        <linearGradient id="beigePanel" x1="0" x2="1">
          <stop offset="0" stop-color="#f8ecdc"/><stop offset="1" stop-color="#e9cfae"/>
        </linearGradient>
      </defs>
      <rect width="680" height="525" fill="url(#beigePanel)"/>
      <polygon points="0,0 460,0 394,110 0,110" fill="url(#brownBand)"/>
      <line x1="18" y1="126" x2="380" y2="126" stroke="#4a3a5a" stroke-width="1.5" stroke-dasharray="4 3"/>
      <line x1="18" y1="305" x2="272" y2="305" stroke="#4a3a5a" stroke-width="1.5" stroke-dasharray="4 3"/>
      <polygon points="0,355 247,355 178,470 0,470" fill="url(#brownBand)"/>
      <polygon points="0,470 178,470 145,525 0,525" fill="#ffffff"/>
      <polygon points="460,0 680,0 680,525 145,525" fill="#ffffff"/>
    </svg>
    <div class="photo" role="img" aria-label="Photo of the lounge with sofas, armchairs and globe pendant lights"
         style="left:305px;top:0;width:375px;height:266px;clip-path:polygon(163px 0,100% 0,100% 100%,0 100%);background:linear-gradient(160deg,#d9c9a8 0%,#b89a72 35%,#5e4330 70%,#3a2a1e 100%)"></div>
    <div class="photo" role="img" aria-label="Photo of the hall with a buffet table, flowers and windows"
         style="left:148px;top:272px;width:532px;height:253px;clip-path:polygon(144px 0,100% 0,100% 100%,0 100%);background:linear-gradient(175deg,#e6dcc4 0%,#c9b08a 40%,#6a4e36 65%,#b5a58c 85%,#8a7358 100%)"></div>

    <div class="brand">El Molinete</div>
    <h1 class="offer"><span class="lead">Check out our special</span><span class="big">Grand Opening<br>pricing!</span></h1>
    <h2 class="hall">El Molinete<span>Reception Hall</span></h2>
    <div class="url">www.el-molinete.example</div>
  </section>

  <section class="card back" aria-label="Postcard back">
    <div class="photo" role="img" aria-label="Faded photo of the main hall with round tables, chairs and string lights"
         style="inset:0;background:radial-gradient(circle at 70% 20%,#f4f4f4 0%,#d8d8d8 45%,#b9b9b9 100%)"></div>
    <svg class="shapes" width="680" height="520" viewBox="0 0 680 520">
      <defs>
        <linearGradient id="panel" x1="0" x2="1">
          <stop offset="0" stop-color="#f8ecdc"/><stop offset="1" stop-color="#e8cda9"/>
        </linearGradient>
        <linearGradient id="foot" x1="0" x2="1">
          <stop offset="0" stop-color="#3e2a1a"/><stop offset=".6" stop-color="#7a5634"/><stop offset="1" stop-color="#4a321e"/>
        </linearGradient>
      </defs>
      <polygon points="0,0 385,0 435,425 0,425" fill="url(#panel)"/>
      <polygon points="60,330 440,330 440,385 60,385 32,357" fill="#4a321e"/>
      <polygon points="440,385 470,425 440,425" fill="#2a1c10"/>
      <rect x="0" y="425" width="470" height="95" fill="url(#foot)"/>
    </svg>

    <div class="tag">About El Molinete</div>
    <div class="details">
      <p><b>Lounge</b> – Beautiful 1,600 ft2 entry room featuring large living room with conversation sofa seating for 40+ Sound system<span class="bullet"></span>Pass-through bar with seating <span class="bullet"></span>Fully-equipped 200 ft2 kitchen with 4-burner gas stove, oven, large double sink, full-size refrigerator, 2 microwaves, and ice machine, plus lots of storage and counter space<span class="bullet"></span>Newly-remodeled Men’s and Women’s bathrooms</p>
      <p><b>Main Hall</b> – Spacious 24’x80’ room with seating for up to 160 people<span class="bullet"></span>2,000 ft2<span class="bullet"></span>72” round tables with chairs, each seating up to 8 guests<span class="bullet"></span>DJ stand and Sound system<span class="bullet"></span>Atmospheric lighting</p>
    </div>
    <div class="ribbon-text">Daytime Parties &amp; Evening Events</div>

    <aside class="pricing" aria-label="Pricing">
      <h3>Pricing</h3>
      <h4>Daytime Parties</h4>
      <div class="when">Available 8AM–2PM · 4-hour minimum</div>
      <div class="area">Lounge and Kitchen Only</div>
      <div class="rate"><span>Fri - Sat - Sun</span><span>$80/hr</span></div>
      <div class="rate"><span>Mon - Thurs</span><span>$60/hr</span></div>
      <div class="area">All Areas: Lounge, Kitchen, Main Hall, and Backyard</div>
      <div class="rate"><span>Fri - Sat - Sun</span><span>$120/hr</span></div>
      <div class="rate"><span>Mon - Thurs</span><span>$100/hr</span></div>
      <hr>
      <h4>Evening Events</h4>
      <div class="when">Available 3PM–12AM · 5-hour minimum</div>
      <div class="area">Lounge and Kitchen Only</div>
      <div class="rate"><span>Fri - Sat - Sun</span><span>$100/hr</span></div>
      <div class="rate"><span>Mon - Thurs</span><span>$50/hr</span></div>
      <div class="area">All Areas</div>
      <div class="rate"><span>Fri - Sat - Sun</span><span>$160/hr</span></div>
      <div class="rate"><span>Mon - Thurs</span><span>$75/hr</span></div>
      <p class="note">Looking for a different time frame, all-day rental, or other special request? Let us know! We'd be happy to provide a custom quote.</p>
    </aside>

    <ul class="contact">
      <li><svg viewBox="0 0 16 16"><path d="M8 1 0 8h2v7h4v-5h4v5h4V8h2z"/></svg>4187C Quillmont Rd, Benicia</li>
      <li><svg viewBox="0 0 16 16"><path d="M4 1 6 5 4.5 6.5c1 2 3 4 5 5L11 10l4 2-1 3C7 15 1 9 1 2z"/></svg>707-555-0142</li>
      <li><svg viewBox="0 0 16 16"><circle cx="8" cy="8" r="7"/></svg>www.El-Molinete.example</li>
    </ul>
    <div class="sign">El Molinete</div>
  </section>

</main>
</body>
</html>
```